Business Card & Logo Design Project

I am looking for a slick/simple design for a logo and business card, for a music Producer/Mixer/Engineer.

I'm based in Tokyo, Japan and I help my clients polish up their creation to major radio/TV status. My clients pay me for my taste, sense of balance expertise and creative direction/

Design should give impression of seal of quality, professionalism, and enthusiasm need some sort of a logo like design for "vantrix productions".

Please don't include music notes or instruments or anything musically related and anything samurai or ninja or too much Japan in them on the design.

I like clever, slick stuff that's not too obvious.
I also like a smooth gradation type transition. My favorite color is deep dark blue/

Good Luck and Thank you for your effort.
Updates

I would like a two-sided design for this one.
One side with "vantrix productions" (all lower case) on, and the other side with my name and contact info.

Please also consider portrait position (or direction).  (as opposed to landscape) 

Target Market(s)

My primary targets are artists & bands, who want absolute best for their creation.

Industry/Entity Type

Business

Requirements
Must have
• Two-Sided
1, vantrix productions
2, Kenji Harumoto, Producer/Mixer/Engineer, +81 090 4827 3516, brambleway@mailnest.example
Nice to have
• Any suggestions are welcome//
Should not have
• Anything music related images.
(e.g. CD, music notations, instruments etc.)

```html
<!DOCTYPE html>
<html lang="en">
<head>
<meta charset="utf-8">
<title>vantrix productions — business card</title>
<link rel="stylesheet" href="https://fonts.googleapis.com/css2?family=Inter:wght@300&display=swap">
<style>
  :root {
    --canvas: #ffffff;
    --card-border: #cccccc;
    --ink: #666666;
    --brand: #b5502c;
  }
  html, body {
    margin: 0;
    padding: 0;
    width: 996px;
    height: 1200px;
    overflow: hidden;
    background: var(--canvas);
    font-family: "Inter", "Helvetica Neue", Arial, sans-serif;
    font-weight: 300;
  }
  .sheet {
    position: relative;
    width: 996px;
    height: 1200px;
  }
  .card {
    position: absolute;
    left: 2px;
    width: 986px;
    box-sizing: border-box;
    border: 3px solid var(--card-border);
    background: var(--canvas);
  }
  .card--front {
    top: 2px;
    height: 570px;
  }
  .card--back {
    top: 630px;
    height: 568px;
  }
  .brand-name {
    position: absolute;
    left: 0;
    right: 0;
    top: 225px;
    margin: 0;
    text-align: center;
    color: var(--brand);
    font-weight: 300;
    line-height: 1;
  }
  .brand-name__main {
    display: block;
    font-size: 84px;
    letter-spacing: 2px;
  }
  .brand-name__sub {
    display: block;
    margin-top: 14px;
    font-size: 26px;
    letter-spacing: 12px;
    padding-left: 12px;
  }
  .contact {
    position: absolute;
    left: 66px;
    top: 143px;
    margin: 0;
    color: var(--ink);
    font-size: 42px;
    line-height: 57px;
    letter-spacing: -0.3px;
  }
  .contact__line {
    display: block;
    white-space: nowrap;
  }
  .contact__gap {
    display: block;
    height: 57px;
  }
</style>
</head>
<body>
  <main class="sheet">
    <section class="card card--front" aria-label="Card front">
      <h1 class="brand-name">
        <span class="brand-name__main">vantrix</span>
        <span class="brand-name__sub">PRODUCTIONS</span>
      </h1>
    </section>

    <section class="card card--back" aria-label="Card back">
      <p class="contact">
        <span class="contact__line contact__name">//kenji harumoto</span>
        <span class="contact__line contact__role">//producer mixer engineer</span>
        <span class="contact__gap" aria-hidden="true"></span>
        <span class="contact__line contact__phone">+81 090 4827 3516</span>
        <span class="contact__line contact__email">brambleway@mailnest.example</span>
      </p>
    </section>
  </main>
</body>
</html>
```